Business Card Project for 'Manufacturing and Healthcare Business Improvement company.

I need a business card for a consulting company that does process improvement for manufacturing and healthcare companies. I had a contest for a logo, and I liked what we came up with for the logo.

I wasn't blown away by what I got for the business card. The designer tried and it was a decent design, but I was looking for a little more. I want something that looks professional, but is eye-catching enough that people say "that looks cool, where did you get it?"

I've uploaded some business card examples I found that I liked. Even though some of the examples have red and orange on them, I think I would stick with blues, grays and blacks since that matches the logo theme. As awesome as some of them look, I don't think that a single color card, like an all-black card, will work for me; but feel free to change my mind.

It might also be possible to incorporate elements from the logo into the card. I also like some of the elements that use circles or rectangles etc to separate the phone number, website etc.

I like it when people have used geometric shapes to break up the card into sections or to add borders to the card to complement the logo, not compete with it for attention. For example, the red and gray example that has a curve that separates the card into two parts. I've wondered, how it would look if the red area were blue and had an arrow separating the top and bottom, like the arrow on the logo. Maybe on the back there could be an element that mirrors the bar graph and arrow. Would those look interesting, or would they compete with the other elements too much?

I also uploaded some examples of cards I made up, either based on ideas I saw elsewhere or based on design elements that the logo had in his designs. If you wonder why the ones with "lorem ipsum" look like an amateur did them, it's because they did.

I also think that I may add a QR code at some point, so I would need a location for that, along with something that says what the QR links to, such as, "scan here to upload contact information" or something similar. I don't know if I want cards that require having special designs cut, but if you have the idea, go with it.

I don't want to limit anyone's creativity, so I'll leave it at that.

Target Market(s)

Healthcare and Manufacturing

Industry/Entity Type

Manufacturing

Contact Information for Business Card

Harborline Advisory Group LLC.
Owen Prescott MBA, LSSMBB
Managing Partner
o.prescott@harborlineadvisorygroupllc.com
(555) 987-2310

Font styles to use
Serif
Sans Serif

Colors

Designer to choose only greyscale colors for use in the design.

Requirements
Must have
• The logo.
Nice to have
• Even though some of the examples I uploaded have red and orange on them, I think I would stick with blues, grays and blacks since that matches the logo theme.

I also like some of the elements that use circles or rectangles etc to separate the phone number, website etc.

I like it when people have used geometric shapes to break up the card into sections or to add borders to the card to complement the logo, not compete with it for attention.

For example, the red and gray example that has a curve that separates the card into two parts. I've wondered, how it would look if the red area were blue and had an arrow separating the top and bottom, like the arrow on the logo. Maybe on the back there could be an element that mirrors the bar graph and arrow. Would those look interesting, or would they compete with the other elements too much?

It might also be possible to incorporate elements from the logo into the card.

I also think that I may add a QR code at some point, so I would need a location for that, along with something that says what the QR links to, such as, "scan here to upload contact information" or something similar.

It could have something somewhere saying "We use Lean, Six Sigma and TPM continuous improvement tools to improve manufacturing and healthcare businesses."
Should not have
• So many colors and elements that it is distracting. Should not be generic.

As awesome as some of them look, I don't think that a single color card, like an all-black card, will work for me; but feel free to change my mind.

I don't know if I want cards that require having special designs cut, but if you have the idea, go with it.

```html
<!DOCTYPE html>
<html lang="en">
<head>
<meta charset="utf-8">
<title>Harborline Advisory Group LLC. – Business Card</title>
<link href="https://fonts.googleapis.com/css2?family=Roboto:wght@400;500;700&display=swap" rel="stylesheet">
<style>
  :root {
    --navy: #1d3466;
    --navy-deep: #142650;
    --navy-light: #3a5590;
    --grey: #6f7378;
    --grey-line: #b9bcc0;
    --white: #ffffff;
    --backdrop: #e9e9ea;
  }
  * { box-sizing: border-box; margin: 0; padding: 0; }
  html, body {
    width: 1200px; height: 716px; overflow: hidden;
    background: var(--backdrop);
    font-family: "Roboto", Arial, sans-serif;
  }
  .stage {
    position: relative; width: 1200px; height: 716px;
    display: flex; align-items: center; justify-content: center; gap: 40px;
  }
  .card {
    position: relative; width: 540px; height: 309px;
    box-shadow: 0 6px 18px rgba(0,0,0,.18);
  }
  /* Front */
  .card-front {
    background: linear-gradient(160deg, var(--navy-deep) 0%, var(--navy) 40%, var(--navy-light) 55%, var(--navy) 70%, var(--navy-deep) 100%);
    display: flex; align-items: center; justify-content: center;
  }
  .brand {
    display: flex; align-items: center; gap: 14px;
    font-weight: 700; text-transform: uppercase; letter-spacing: .5px;
    line-height: 1.05;
  }
  .brand-mark { width: 18px; height: 18px; flex: none; }
  .card-front .brand { color: var(--white); font-size: 30px; }
  .card-front .brand-mark { width: 26px; height: 26px; background: var(--white); }
  /* Back */
  .card-back {
    background: var(--white);
    border-bottom: 3px solid var(--navy);
    display: grid; grid-template-columns: 250px 1px 1fr;
    align-items: center; padding: 0 18px 0 26px;
  }
  .card-back .brand { color: var(--navy); font-size: 19px; gap: 10px; }
  .card-back .brand-mark { background: var(--navy); }
  .divider { width: 1px; height: 150px; background: var(--grey-line); }
  .details { padding-left: 18px; }
  .person-name { color: var(--navy); font-weight: 700; font-size: 15px; text-transform: uppercase; letter-spacing: .3px; }
  .person-role { color: var(--grey); font-size: 10.5px; margin-top: 3px; }
  .address { color: var(--grey); font-size: 10.5px; line-height: 1.5; margin-top: 12px; }
  .contact-list { list-style: none; margin-top: 10px; }
  .contact-list li {
    display: flex; align-items: center; gap: 8px;
    font-size: 10px; color: var(--grey); line-height: 1.9; white-space: nowrap;
  }
  .contact-list li.web { color: var(--navy); }
  .contact-list svg { width: 11px; height: 11px; flex: none; fill: none; stroke: var(--navy); stroke-width: 2; }
</style>
</head>
<body>
<main class="stage">
  <section class="card card-front" aria-label="Card front">
    <div class="brand"><span class="brand-mark"></span><span>Harborline Advisory<br>Group LLC.</span></div>
  </section>

  <section class="card card-back" aria-label="Card back">
    <div class="brand"><span class="brand-mark"></span><span>Harborline Advisory<br>Group LLC.</span></div>
    <div class="divider"></div>
    <div class="details">
      <h1 class="person-name">Owen Prescott MBA, LSSMBB</h1>
      <p class="person-role">Managing Partner</p>
      <p class="address">Your address, city<br>state, ZIP 0000</p>
      <ul class="contact-list">
        <li>
          <svg viewBox="0 0 24 24"><path d="M5 3h4l2 5-3 2a12 12 0 0 0 6 6l2-3 5 2v4a2 2 0 0 1-2 2A17 17 0 0 1 3 5a2 2 0 0 1 2-2z" fill="#1d3466" stroke="none"/></svg>
          (555) 987-2310
        </li>
        <li>
          <svg viewBox="0 0 24 24"><rect x="2" y="5" width="20" height="14" rx="1"/><path d="M2 6l10 7 10-7"/></svg>
          o.prescott@harborlineadvisorygroupllc.com
        </li>
        <li class="web">
          <svg viewBox="0 0 24 24"><circle cx="12" cy="12" r="10"/><path d="M2 12h20M12 2c3 3 3 17 0 20M12 2c-3 3-3 17 0 20"/></svg>
          www.harborlineadvisorygroupllc.com
        </li>
      </ul>
    </div>
  </section>
</main>
</body>
</html>
```